Ferncrest Dental, LLC business card project

Business card to be designed with current logo.
Dental office- please keep design of card that looks clean and professional.
Please include the following info:
Ferncrest Dental, LLC
Dr. Lorna Pettigrew
2871 Marlowe Street
Bethlehem, PA 18093
610-555-0193
ferncrestdental.office@examplemail.test
Hello everyone-
Reason: Just got back from overseas- will look at all designs and provide feedback. Thank you!
Reason: Polling my friends for the final selection-
thank you to all those that participated- so many talented designers!

```html
<!DOCTYPE html>
<html lang="en">
<head>
<meta charset="utf-8">
<title>Ferncrest Dental, LLC — Business Card</title>
<link href="https://fonts.googleapis.com/css2?family=Abel&display=swap" rel="stylesheet">
<style>
  :root {
    --page-bg: #ffffff;
    --card-bg: #ffffff;
    --card-edge: #5a5a5a;
    --brand-green: #6a9e43;
    --band-green: #66a043;
    --band-text: #ffffff;
    --window-light: #ffffff;
    --window-dark: #d8d9db;
  }
  * { margin: 0; padding: 0; box-sizing: border-box; }
  html, body {
    width: 1200px;
    height: 1000px;
    overflow: hidden;
    background: var(--page-bg);
    font-family: "Abel", sans-serif;
  }
  .business-card {
    position: absolute;
    left: 240px;
    top: 175px;
    width: 716px;
    height: 463px;
    background: var(--card-bg);
    border: 1px solid var(--card-edge);
  }
  .brand {
    position: absolute;
    left: 30px;
    top: 20px;
    display: flex;
    align-items: center;
    gap: 16px;
  }
  .brand-dot {
    width: 30px;
    height: 30px;
    border-radius: 50%;
    background: var(--brand-green);
  }
  .brand-name {
    font-size: 48px;
    line-height: 60px;
    color: var(--brand-green);
    font-weight: 400;
    letter-spacing: -0.5px;
  }
  .photo-window {
    position: absolute;
    left: 47px;
    top: 140px;
    width: 635px;
    height: 198px;
    border-radius: 0 46px 46px 0;
    background: linear-gradient(to right, var(--window-light) 0%, #f1f1f2 25%, var(--window-dark) 100%);
  }
  .contact-band {
    position: absolute;
    left: 0;
    right: 0;
    top: 362px;
    height: 92px;
    background: var(--band-green);
    color: var(--band-text);
    padding: 8px 18px 0;
  }
  .doctor-name {
    font-size: 25px;
    line-height: 30px;
    letter-spacing: 0.3px;
  }
  .contact-line {
    font-size: 17px;
    line-height: 22px;
    letter-spacing: 0.2px;
  }
  .office-address {
    position: absolute;
    right: 18px;
    bottom: 10px;
    font-size: 16px;
    line-height: 22px;
    letter-spacing: 0.3px;
  }
</style>
</head>
<body>
  <article class="business-card">
    <header class="brand">
      <span class="brand-dot" aria-hidden="true"></span>
      <span class="brand-name">Ferncrest Dental, LLC</span>
    </header>

    <div class="photo-window" role="img" aria-label="Window panel for a smiling-patient photo in soft grey tones"></div>

    <footer class="contact-band">
      <p class="doctor-name">Dr. Lorna Pettigrew</p>
      <p class="contact-line">ferncrestdental.office@examplemail.test</p>
      <p class="contact-line">Tel: 610-555-0193</p>
      <p class="office-address">Ferncrest Dental, LLC, 2871 Marlowe Street, Bethlehem, PA 18093.</p>
    </footer>
  </article>
</body>
</html>
```